Cedarbrook Residences - Billboard design for our newly renovated townhome community

We have a 5' wide x 4' tall billboard at the entrance to our apartment community, that needs to have the acrylic insert replaced. It is a 2 sided sign, and we are planning to use the same image on both sides. We are called Cedarbrook Residences, and have 48 townhomes that are all 2 bedroom, 1 1/2 bath. A few things we would like to get across on the signage: "Newly Renovated" "2 bed 1 1/2 bath" "Full size W/D in every home" " New Appliances" I've included our parent company's logo - this is the only image I could think of, but it might not be worth having it on the sign. We are in Colorado, so mountain theme could be nice and also sunshine/sun since we are called "Cedarbrook"

Industry/Entity Type

Apartment

Font styles to use
Sans Serif

Requirements
Must have
• Newly Renovated
2 bed 1 1/2 bath
Full size W/D in every home
Virtual Tours available
www.marlowepeaksliving.com
855 - 413 - 9268
Nice to have
• We are located in Colorado - possibly mountain theme? Since our community is called "Cedarbrook Residences" - anything bright with Sun / Sunshine might look really nice as well.

```html
<!DOCTYPE html>
<html lang="en">
<head>
<meta charset="utf-8">
<title>Cedarbrook Residences – Entrance Sign</title>
<link rel="stylesheet" href="https://fonts.googleapis.com/css2?family=Archivo+Black&family=Montserrat:wght@800&family=Oswald:wght@600&display=swap">
<style>
  :root {
    --page-bg: #efefef;
    --sky-top: #e9eef4;
    --sky-mid: #a9c2d6;
    --peak: #7d7690;
    --forest: #2f3a2c;
    --autumn: #8a6a2a;
    --lake: #3d3a36;
    --headline-yellow: #fff200;
    --headline-white: #ffffff;
    --outline-black: #121212;
    --band-blue: #00aeef;
    --band-dark: #262626;
    --badge-red: #e0141c;
    --badge-red-deep: #8e0a0f;
    --badge-ring: #d9d9d9;
    --tick-yellow: #ffe500;
    --brand-ink: #1c1c1c;
  }
  * { margin: 0; padding: 0; box-sizing: border-box; }
  html, body { width: 1200px; height: 1101px; overflow: hidden; }
  body { background: var(--page-bg); position: relative; }

  .sign {
    position: absolute; left: 20px; top: 91px;
    width: 1160px; height: 918px; overflow: hidden;
    font-family: "Montserrat", sans-serif;
  }
  .sign__scenery {
    position: absolute; inset: 0;
    background:
      linear-gradient(180deg, var(--sky-top) 0%, var(--sky-mid) 28%, var(--peak) 42%, var(--forest) 58%, var(--autumn) 68%, var(--lake) 80%, #23211f 100%);
  }
  .brand {
    position: absolute; top: 160px; left: 0; width: 100%;
    text-align: center; font-weight: 800; font-size: 34px;
    color: var(--brand-ink); letter-spacing: 1px;
  }
  .headline {
    position: absolute; left: 0; width: 100%; text-align: center;
    font-family: "Archivo Black", sans-serif; line-height: 1;
    paint-order: stroke fill; -webkit-text-stroke: 12px var(--outline-black);
    text-shadow: 6px 7px 0 var(--outline-black);
  }
  .headline--newly { top: 336px; font-size: 136px; color: var(--headline-yellow); letter-spacing: 2px; left: -10px; }
  .headline--renovated { top: 452px; font-size: 128px; color: var(--headline-white); letter-spacing: 1px; left: 6px; }

  .features { position: absolute; left: 84px; top: 600px; list-style: none; }
  .features__item {
    display: flex; align-items: center; gap: 14px;
    color: #fff; font-size: 35px; line-height: 58px; letter-spacing: -0.5px;
    text-shadow: 2px 2px 4px rgba(0,0,0,.6);
  }
  .features__tick { width: 34px; height: 34px; flex: none; }

  .contact-phone {
    position: absolute; left: 0; top: 734px; width: 100%; height: 106px;
    background: var(--band-blue);
  }
  .contact-phone__icon { position: absolute; left: 28px; top: 18px; width: 72px; height: 72px; }
  .contact-phone__number {
    position: absolute; left: 134px; top: 4px;
    font-size: 104px; line-height: 100px; color: #fff; letter-spacing: -2px;
  }
  .contact-web {
    position: absolute; left: 0; top: 840px; width: 100%; height: 78px;
    background: var(--band-dark);
  }
  .contact-web__icon { position: absolute; left: 42px; top: 20px; width: 40px; height: 40px; }
  .contact-web__url {
    position: absolute; left: 134px; top: 18px;
    font-size: 40px; line-height: 44px; color: #fff; letter-spacing: -0.5px;
  }

  .tour-badge {
    position: absolute; left: 896px; top: 654px; width: 248px; height: 248px;
    border-radius: 50%; background: var(--badge-ring);
    box-shadow: 0 3px 8px rgba(0,0,0,.4);
  }
  .tour-badge__face {
    position: absolute; inset: 12px; border-radius: 50%; overflow: hidden;
    background: radial-gradient(circle at 50% 30%, var(--badge-red) 0%, var(--badge-red) 55%, var(--badge-red-deep) 100%);
    text-align: center; font-family: "Oswald", sans-serif; color: #fff;
  }
  .tour-badge__main { margin-top: 44px; font-size: 56px; line-height: 50px; letter-spacing: -1px; }
  .tour-badge__strip {
    margin-top: 10px; background: var(--band-dark);
    font-size: 32px; line-height: 48px;
  }
</style>
</head>
<body>
  <main class="sign">
    <div class="sign__scenery" role="img" aria-label="Colorado mountain valley with snowy peaks, evergreen and autumn forest, and an alpine lake"></div>

    <p class="brand">Alderpeak Communities</p>

    <h1>
      <span class="headline headline--newly">NEWLY</span>
      <span class="headline headline--renovated">RENOVATED</span>
    </h1>

    <ul class="features">
      <li class="features__item">
        <svg class="features__tick" viewBox="0 0 34 34"><circle cx="17" cy="17" r="14" fill="none" stroke="var(--tick-yellow)" stroke-width="3.5"/><path d="M10.5 17.5l4.5 4.5 8.5-9" fill="none" stroke="var(--tick-yellow)" stroke-width="3.5" stroke-linecap="round" stroke-linejoin="round"/></svg>
        2 BED 1 1/2 BATH
      </li>
      <li class="features__item">
        <svg class="features__tick" viewBox="0 0 34 34"><circle cx="17" cy="17" r="14" fill="none" stroke="var(--tick-yellow)" stroke-width="3.5"/><path d="M10.5 17.5l4.5 4.5 8.5-9" fill="none" stroke="var(--tick-yellow)" stroke-width="3.5" stroke-linecap="round" stroke-linejoin="round"/></svg>
        FULL SIZE W/D IN EVERY HOME
      </li>
    </ul>

    <div class="contact-phone">
      <svg class="contact-phone__icon" viewBox="0 0 72 72"><circle cx="36" cy="36" r="31" fill="none" stroke="#fff" stroke-width="5"/><path d="M24 20c2-2 4-2 5 0l4 7c1 2 0 3-1 4l-2 2c2 5 6 9 11 11l2-2c1-1 2-2 4-1l7 4c2 1 2 3 0 5l-3 3c-3 3-9 2-16-4s-10-13-9-18z" fill="#fff"/></svg>
      <span class="contact-phone__number">855-413-9268</span>
    </div>

    <div class="contact-web">
      <svg class="contact-web__icon" viewBox="0 0 40 40" fill="none" stroke="#fff" stroke-width="2.5"><circle cx="20" cy="20" r="17"/><ellipse cx="20" cy="20" rx="7.5" ry="17"/><path d="M3 20h34M6 11h28M6 29h28"/></svg>
      <span class="contact-web__url">WWW.MARLOWEPEAKSLIVING.COM</span>
    </div>

    <div class="tour-badge">
      <div class="tour-badge__face">
        <p class="tour-badge__main">VIRTUAL<br>TOURS</p>
        <p class="tour-badge__strip">AVAILABLE</p>
      </div>
    </div>
  </main>
</body>
</html>
```